Brenwick Drilling Inc. Business card design

Business card design for "Brenwick Drilling Inc. - Directional Drilling Services"

Address is:

Brenwick Drilling Inc.
512 - 73 Tolvane Crescent SW
Calgary, Alberta, Canada
T2K 4P8

Please incorporate the logo design into the card, thank you.

Target Market(s)

Oil & Gas and Drilling

Industry/Entity Type

Business

```html
<!DOCTYPE html>
<html lang="en">
<head>
<meta charset="utf-8">
<title>Brenwick Drilling Inc. – Business Card</title>
<link href="https://fonts.googleapis.com/css2?family=Michroma&family=Exo+2:wght@400&display=swap" rel="stylesheet">
<style>
  :root {
    --stage: #fdfdfd;
    --stage-edge: #f1f1f1;
    --ink-black: #0c0c0c;
    --band-grey: #222222;
    --accent-red: #d42a10;
    --card-red: #cc2208;
    --card-red-glow: #de3312;
    --card-red-edge: #b91c06;
    --paper: #ffffff;
    --paper-shade: #ececec;
    --text-dark: #2a2a2a;
    --text-light: #ffffff;
  }
  * { margin: 0; padding: 0; box-sizing: border-box; }
  html, body { width: 1200px; height: 900px; overflow: hidden; }
  body {
    background: var(--stage-edge);
    position: relative;
  }
  .stage {
    position: absolute;
    left: 28px; top: 20px; width: 1145px; height: 860px;
    background: radial-gradient(ellipse at center, var(--stage) 55%, var(--stage-edge) 100%);
  }
  .card {
    position: absolute;
    top: 306px;
    width: 474px;
    height: 290px;
    overflow: hidden;
    box-shadow: 3px 5px 6px rgba(0,0,0,0.28);
  }
  .card--front {
    left: 98px;
    background: linear-gradient(135deg, var(--paper) 60%, var(--paper-shade) 100%);
  }
  .card--back {
    left: 629px;
    background: radial-gradient(ellipse at 45% 50%, var(--card-red-glow) 0%, var(--card-red) 45%, var(--card-red-edge) 100%);
  }
  .front-panels { position: absolute; inset: 0; }
  .brand {
    position: absolute;
    display: flex;
    flex-direction: column;
    align-items: center;
    color: var(--text-light);
  }
  .card--front .brand { left: 34px; top: 108px; width: 180px; }
  .card--back .brand { left: 0; top: 104px; width: 474px; }
  .brand-dot {
    width: 34px; height: 34px; border-radius: 50%;
    margin-bottom: 30px;
  }
  .card--front .brand-dot { background: var(--accent-red); }
  .card--back .brand-dot { background: var(--text-light); }
  .brand-name {
    font-family: "Michroma", sans-serif;
    font-size: 11.5px;
    letter-spacing: 0.3px;
    white-space: nowrap;
    line-height: 1;
  }
  .brand-tagline {
    font-family: "Exo 2", sans-serif;
    font-size: 6.6px;
    letter-spacing: 2.1px;
    text-transform: uppercase;
    white-space: nowrap;
    margin-top: 3px;
  }
  .address {
    position: absolute;
    right: 18px;
    top: 128px;
    text-align: right;
    font-family: "Exo 2", sans-serif;
    font-size: 12.5px;
    line-height: 16px;
    color: var(--text-dark);
    font-style: normal;
  }
</style>
</head>
<body>
  <div class="stage"></div>

  <section class="card card--front" aria-label="Business card front">
    <svg class="front-panels" width="474" height="290" viewBox="0 0 474 290" aria-hidden="true">
      <polygon points="0,0 240,0 280,290 0,290" fill="var(--ink-black)"/>
      <polygon points="0,252 275,252 280,290 0,290" fill="var(--band-grey)"/>
      <polygon points="240,0 279,0 267,190" fill="var(--accent-red)"/>
    </svg>
    <div class="brand">
      <span class="brand-dot"></span>
      <span class="brand-name">BRENWICK DRILLING INC.</span>
      <span class="brand-tagline">Directional Drilling Services</span>
    </div>
    <address class="address">
      512 - 73 Tolvane Crescent SW<br>
      Calgary, Alberta, Canada<br>
      T2K 4P8
    </address>
  </section>

  <section class="card card--back" aria-label="Business card back">
    <div class="brand">
      <span class="brand-dot"></span>
      <span class="brand-name">BRENWICK DRILLING INC.</span>
      <span class="brand-tagline">Directional Drilling Services</span>
    </div>
  </section>
</body>
</html>
```